Corvane Strategy Partners Marketing Audit Teaser

Design a 1-page (2-sided) teaser on the Corvane Strategy Partners Marketing Audit. A Project Brief; Copy document; logo file; and picture file will be provided to further detail what is required. Additional logo files are available, if needed, depending on the designers recommendations.

```html
<!DOCTYPE html>
<html lang="en">
<head>
<meta charset="utf-8">
<title>Corvane Strategy Partners Marketing Audit Teaser</title>
<link href="https://fonts.googleapis.com/css2?family=Inter:wght@400;500;700&display=swap" rel="stylesheet">
<style>
  :root {
    --backdrop: #e4e4e4;
    --paper: #ffffff;
    --ink: #121212;
    --navy: #131e2e;
    --yellow: #f1b12b;
    --green: #47b07a;
    --red: #e6523a;
    --rule: #c9c9c9;
    --muted: #4a4a4a;
  }
  * { margin: 0; padding: 0; box-sizing: border-box; }
  html, body { width: 1200px; height: 1200px; overflow: hidden; }
  body {
    background: var(--backdrop);
    font-family: "Inter", Arial, sans-serif;
    color: var(--ink);
    position: relative;
  }
  .teaser {
    position: absolute;
    left: 205px; top: 40px;
    width: 790px; height: 1120px;
    background: var(--paper);
    overflow: hidden;
  }
  .abs { position: absolute; }

  .brand {
    left: 55px; top: 70px;
    font-size: 28px; font-weight: 400; letter-spacing: 0.2px;
    display: flex; align-items: center; gap: 10px;
  }
  .brand-square { width: 18px; height: 18px; background: var(--ink); }

  .header-divider { left: 498px; top: 69px; width: 1px; height: 66px; background: var(--rule); }
  .header-title { left: 536px; top: 70px; font-size: 14px; line-height: 22px; color: var(--ink); }

  .headline {
    left: 55px; top: 226px;
    font-size: 67px; font-weight: 700; line-height: 72px; letter-spacing: -0.5px;
  }
  .headline-rule { left: 54px; top: 505px; width: 307px; height: 1px; background: var(--rule); }
  .intro {
    left: 54px; top: 538px; width: 320px;
    font-size: 14px; line-height: 20px; color: var(--muted);
  }

  .graphics { left: 0; top: 0; width: 790px; height: 1120px; }

  .info-panel {
    left: 0; top: 907px; width: 394px; height: 213px;
    background: var(--navy); color: #fff;
  }
  .info-col { position: absolute; top: 62px; }
  .info-col.first { left: 52px; }
  .info-col.second { left: 237px; }
  .info-divider { position: absolute; left: 205px; top: 47px; width: 1px; height: 117px; background: #55607a; }
  .info-label { font-size: 9px; letter-spacing: 1px; font-weight: 500; color: #b9c0cc; display: flex; align-items: center; gap: 5px; height: 12px; }
  .info-label.accent { color: var(--yellow); }
  .info-label .dot { width: 7px; height: 7px; background: var(--yellow); }
  .info-sub { margin-top: 17px; font-size: 11px; letter-spacing: 0.4px; color: #d7dbe2; }
  .info-item { font-size: 13px; line-height: 20px; color: #fff; margin-top: 3px; }

  .steps { left: 563px; top: 962px; }
  .step { display: flex; align-items: baseline; height: 33px; }
  .step-num { width: 40px; font-size: 13px; color: var(--muted); }
  .step-name { font-size: 21px; font-weight: 500; }
</style>
</head>
<body>
  <main class="teaser">
    <svg class="abs graphics" viewBox="0 0 790 1120" width="790" height="1120">
      <defs>
        <linearGradient id="fruitTone" x1="0" y1="0" x2="1" y2="1">
          <stop offset="0" stop-color="#f1b12b"/>
          <stop offset="0.45" stop-color="#8a6a1c"/>
          <stop offset="1" stop-color="#3b3212"/>
        </linearGradient>
        <linearGradient id="greenTone" x1="0" y1="0" x2="1" y2="1">
          <stop offset="0" stop-color="#4cb47f"/>
          <stop offset="1" stop-color="#2d7a55"/>
        </linearGradient>
      </defs>
      <!-- navy corner behind curve -->
      <rect x="340" y="560" width="158" height="170" fill="var(--navy)"/>
      <path d="M0 560 H498 V584 Q498 727 355 727 H0 Z" fill="var(--paper)"/>
      <!-- right column -->
      <path d="M498 319 A146 146 0 0 1 790 319 V541 H498 Z" fill="url(#fruitTone)" role="img" aria-label="Duotone photo of a fruit on yellow"/>
      <rect x="498" y="541" width="292" height="366" fill="url(#greenTone)" role="img" aria-label="Duotone photo of a consultant in a suit on green"/>
      <!-- bottom row shapes -->
      <path d="M290 727 H498 V807 Q498 907 398 907 H290 Z" fill="var(--yellow)"/>
      <path d="M187 727 H290 V817 H394 Q394 907 290 907 H187 Z" fill="var(--red)"/>
      <circle cx="93" cy="817" r="93" fill="url(#greenTone)" role="img" aria-label="Duotone portrait of a team member on green"/>
    </svg>

    <div class="abs brand"><span class="brand-square"></span>Corvane</div>
    <div class="abs header-divider"></div>
    <p class="abs header-title">Corvane Strategy Partners<br>Marketing Audit</p>

    <h1 class="abs headline">Teaser<br>Marketing<br>Audit</h1>
    <div class="abs headline-rule"></div>
    <p class="abs intro">Our audit reviews your brand, channels and messaging to surface quick wins and long-term growth levers. In four weeks we map the full funnel, benchmark against peers and deliver a clear, prioritised recommendations report.</p>

    <section class="abs info-panel">
      <div class="info-col first">
        <div class="info-label accent">SCOPE <span class="dot"></span></div>
        <div class="info-sub">CORE AREAS</div>
        <div class="info-item">Brand Positioning<br>Channels</div>
      </div>
      <div class="info-divider"></div>
      <div class="info-col second">
        <div class="info-label">WHAT YOU GET</div>
        <div class="info-sub">DELIVERABLES</div>
        <div class="info-item">Prioritised Plan<br>Key Insights</div>
      </div>
    </section>

    <ol class="abs steps">
      <li class="step"><span class="step-num">34</span><span class="step-name">Research</span></li>
      <li class="step"><span class="step-num">72</span><span class="step-name">Mapping</span></li>
      <li class="step"><span class="step-num">38</span><span class="step-name">Counsel</span></li>
    </ol>
  </main>
</body>
</html>
```